Logo, Business Card & Stationery Design Project

Firstly, we need a quick turnaround for this project.
The company is KLT Financial.
KLT Financial specialises in sourcing, marketing and introducing clients to hassle free investment property opportunities. We are looking for a design representing stability, professionalism and customer focused. We also need to have the feel of being approachable and practical.
The design will be for the logo initially followed by business cards, letterhead (inc word based doc), with compliments, envelopes, stickers and Word documents for a letterhead & title page.
We look forward to seeing your designs.
Target Market(s)
Generally middle class couples aged from 30-50
Industry/Entity Type
Investment
Look and feel
Each slider illustrates characteristics of the customer's brand and the style your logo design should communicate.

```html
<!DOCTYPE html>
<html lang="en">
<head>
<meta charset="UTF-8">
<title>KLT Financial – Business Card</title>
<link rel="stylesheet" href="https://fonts.googleapis.com/css2?family=Tinos&display=swap">
<style>
  :root {
    --navy: #163a58;
    --ink: #3f4650;
    --muted: #b7b6c6;
    --silver: #b1b0bf;
    --paper: #ffffff;
    --edge: #d2d2d6;
  }
  * { margin: 0; padding: 0; box-sizing: border-box; }
  html, body {
    width: 1200px;
    height: 900px;
    overflow: hidden;
    background: var(--paper);
  }
  .canvas {
    position: relative;
    width: 1200px;
    height: 900px;
    font-family: "Tinos", "Times New Roman", serif;
  }
  .card {
    position: absolute;
    left: 328px;
    width: 736px;
  }
  .card-front {
    top: 20px;
    height: 418px;
    background: radial-gradient(ellipse 62% 78% at 50% 45%, #ffffff 0%, #f1f1f4 30%, #d3d2dc 65%, var(--silver) 100%);
  }
  .card-back {
    top: 450px;
    height: 422px;
    background: var(--paper);
    border: 2px solid var(--edge);
  }
  .brand-name {
    position: absolute;
    color: var(--navy);
    font-weight: 400;
    white-space: nowrap;
  }
  .card-front .brand-name {
    left: 0;
    right: 0;
    top: 160px;
    text-align: center;
    font-size: 68px;
    letter-spacing: 2px;
  }
  .card-back .brand-name {
    right: 34px;
    top: 300px;
    font-size: 32px;
    letter-spacing: 1px;
  }
  .person-name {
    position: absolute;
    left: 52px;
    top: 42px;
    font-size: 52px;
    color: var(--navy);
    font-weight: 400;
  }
  .person-role {
    position: absolute;
    left: 52px;
    top: 106px;
    font-size: 40px;
    color: var(--navy);
  }
  .contact {
    position: absolute;
    left: 52px;
    top: 222px;
    list-style: none;
    font-size: 26px;
    line-height: 41px;
  }
  .contact .address { color: var(--ink); }
  .contact .reach { color: var(--muted); }
</style>
</head>
<body>
  <main class="canvas">
    <section class="card card-front" aria-label="Card front">
      <p class="brand-name">KLT Financial</p>
    </section>

    <section class="card card-back" aria-label="Card back">
      <h1 class="person-name">Name Name</h1>
      <p class="person-role">Position</p>
      <ul class="contact">
        <li class="address">2870 Elm Avenue</li>
        <li class="address">City</li>
        <li class="reach">555.014.2938</li>
        <li class="reach">emailaddress@email.com</li>
      </ul>
      <p class="brand-name">KLT Financial</p>
    </section>
  </main>
</body>
</html>
```